Computer repair shop

A card with our logo. And number and email and address. Our colors are baby /light blue and gray

Prefferably one sode with full logo - interested in other designs and options

Computer / mac repair shop
On site support
Snall business IT support

```html
<!DOCTYPE html>
<html lang="en">
<head>
<meta charset="utf-8">
<title>ByteFix Repair – Business Card</title>
<link href="https://fonts.googleapis.com/css2?family=Open+Sans:wght@400;600;700&display=swap" rel="stylesheet">
<style>
  :root {
    --backdrop: #d9dcdf;
    --card: #ffffff;
    --ink: #1e1e1e;
    --ink-soft: #3a3a3a;
    --brand-blue: #2b9bd8;
    --rule: #2a2a2a;
  }
  * { box-sizing: border-box; margin: 0; padding: 0; }
  html, body {
    width: 1200px; height: 800px; overflow: hidden;
    background: var(--backdrop);
    font-family: "Open Sans", sans-serif;
    color: var(--ink);
  }
  .stage {
    width: 1200px; height: 800px;
    display: flex; flex-direction: column;
    align-items: center; justify-content: center; gap: 36px;
  }
  .card {
    width: 600px; height: 343px;
    background: var(--card);
    box-shadow: 0 6px 18px rgba(0,0,0,0.18);
    position: relative;
  }
  .brand {
    display: flex; align-items: center; justify-content: center; gap: 14px;
  }
  .brand-mark {
    width: 34px; height: 34px; background: var(--brand-blue);
  }
  .brand-name {
    font-weight: 700; color: var(--brand-blue);
    letter-spacing: 0.5px;
  }

  /* Front */
  .card-front .brand { position: absolute; top: 104px; left: 0; right: 0; }
  .card-front .brand-name { font-size: 44px; }
  .tagline {
    position: absolute; left: 0; right: 0; top: 228px;
    text-align: center; font-size: 15px; color: var(--ink-soft);
  }
  .tagline .sep { color: var(--brand-blue); margin: 0 5px; }

  /* Back */
  .card-back .brand { position: absolute; top: 52px; left: 0; right: 0; }
  .card-back .brand-mark { width: 28px; height: 28px; }
  .card-back .brand-name { font-size: 34px; }
  .contact-row {
    position: absolute; top: 170px; left: 0; right: 0;
    display: flex; justify-content: center; align-items: stretch;
  }
  .person { text-align: right; padding-right: 20px; padding-top: 2px; }
  .person-name { color: var(--brand-blue); font-size: 22px; font-weight: 600; }
  .person-role { font-size: 16px; color: var(--ink-soft); }
  .divider { width: 1.5px; background: var(--rule); }
  .details { list-style: none; padding-left: 16px; font-size: 16px; line-height: 24px; color: var(--ink); }
  .details li { display: flex; align-items: center; gap: 8px; }
  .details svg { width: 14px; height: 14px; fill: none; stroke: var(--brand-blue); stroke-width: 1.6; }
  .details .icon-phone { fill: var(--brand-blue); stroke: none; }
  .address {
    position: absolute; top: 268px; left: 0; right: 0;
    text-align: center; font-size: 16px; color: var(--ink);
  }
</style>
</head>
<body>
<main class="stage">
  <section class="card card-front">
    <div class="brand">
      <span class="brand-mark"></span>
      <span class="brand-name">ByteFix Repair</span>
    </div>
    <p class="tagline">Computer / mac repair shop<span class="sep">|</span>On site support<span class="sep">|</span>Snall business IT support</p>
  </section>

  <section class="card card-back">
    <div class="brand">
      <span class="brand-mark"></span>
      <span class="brand-name">ByteFix Repair</span>
    </div>
    <div class="contact-row">
      <div class="person">
        <p class="person-name">Daniel Carter</p>
        <p class="person-role">Owner</p>
      </div>
      <div class="divider"></div>
      <ul class="details">
        <li>
          <svg class="icon-phone" viewBox="0 0 16 16"><path d="M3.6 1.2l2.3 2.6-1.3 2a9 9 0 0 0 5.6 5.6l2-1.3 2.6 2.3-1.3 2.4C7.4 15.2.8 8.6 1.2 2.5z"/></svg>
          +1 (555) 214-0386
        </li>
        <li>
          <svg viewBox="0 0 16 16"><rect x="1.5" y="3.5" width="13" height="9"/><path d="M1.5 3.5l6.5 5 6.5-5"/></svg>
          daniel@bytefixrepair.com
        </li>
        <li>
          <svg viewBox="0 0 16 16"><circle cx="8" cy="8" r="6.5"/><ellipse cx="8" cy="8" rx="2.8" ry="6.5"/><path d="M1.5 8h13"/></svg>
          www.bytefixrepair.com
        </li>
      </ul>
    </div>
    <p class="address">4820 Maple Ridge Ave #12, Lakeview WA 98000</p>
  </section>
</main>
</body>
</html>
```